Re-design of veterinary clinic website *

For a future relaunch of our webpage, we would like to find a fresh design that still incorporates the spirit of our current one which can be found at http://dr-wenzlaff.de
We are a small business that appeals to locals but are known in a wide area for specialist services.
According to analytics data, most people rarely read through the full website but are using it to inform themselves about opening hours, Telephone numbers and location. Still, the website needs to offer enough content to be ranked positively by the Quandle algorithm.
Our logo is not part of the re-design but needs to be included in your proposal as is. It can be used a source of inspiration, just as the current design. Keep in mind, that the design will be used as the basis of a fluid webdesign for both mobile and desktop. Roughly 75% of our users are on mobile devices.
Target Market(s)
Locals
Industry/Entity Type
Veterinary
Number of Pages Required
1 page
Look and feel
Each slider illustrates characteristics of the customer's brand and the style your logo design should communicate.

```html
<!DOCTYPE html>
<html lang="en">
<head>
<meta charset="utf-8">
<title>Helmut Wenzlaff – Veterinary Clinic</title>
<link rel="stylesheet" href="https://fonts.googleapis.com/css2?family=Josefin+Sans:wght@300;400;600&family=Lato:wght@300;400;700&family=Oswald:wght@500&display=swap">
<style>
:root{
  --navy:#283e8c;
  --royal:#0a52a8;
  --sky:#85c6e6;
  --ink:#3b3b3b;
  --muted:#8a8a8a;
  --grey-bg:#f6f6f6;
  --white:#ffffff;
  --footer:#0a4ea2;
  --copyright:#666666;
}
*{margin:0;padding:0;box-sizing:border-box}
html,body{width:1200px;height:3396px;overflow:hidden}
body{position:relative;background:var(--white);font-family:"Lato",sans-serif;color:var(--ink)}
.abs{position:absolute}

/* header */
.brand{left:72px;top:46px;display:flex;align-items:center;gap:18px}
.brand-dot{width:54px;height:54px;border-radius:50%;border:3px solid var(--navy)}
.brand-name{font-family:"Josefin Sans",sans-serif;font-weight:600;font-size:40px;color:var(--navy);letter-spacing:2px}
.nav{left:0;top:154px;width:1200px;height:45px;background:var(--navy);display:flex;padding-left:170px}
.nav a{display:block;height:45px;line-height:47px;color:var(--white);text-decoration:none;font-family:"Josefin Sans",sans-serif;font-size:16px;text-align:center;padding:0 26px}
.nav a.active{background:var(--sky);width:97px;padding:0}

/* hero */
.hero{left:0;top:199px;width:1200px;height:446px;background:linear-gradient(100deg,#dfe8f2 0%,#eef3f8 40%,#f7f7f7 65%,#cfdbe6 100%)}
.hero-title{left:72px;top:312px;font-family:"Josefin Sans",sans-serif;font-size:46px;color:var(--royal);font-weight:400;letter-spacing:1px}
.hero-sub{left:74px;top:366px;font-family:"Josefin Sans",sans-serif;font-size:19px;color:var(--royal);font-weight:300}
.hero-text{left:78px;top:406px;width:440px;font-size:13px;line-height:26px;color:#333}
.btn{display:block;background:var(--navy);color:var(--white);text-align:center;font-size:14px;text-decoration:none}
.hero-btn{left:72px;top:503px;width:222px;height:47px;line-height:47px}

/* welcome + hours */
.welcome-title{left:74px;top:730px;font-family:"Josefin Sans",sans-serif;font-size:38px;font-weight:300;color:#6b6b6b;letter-spacing:1px}
.welcome-kicker{left:74px;top:823px;font-family:"Josefin Sans",sans-serif;font-size:20px;font-weight:400;color:var(--royal)}
.welcome-text{left:74px;top:860px;width:440px;font-size:14px;line-height:24px;color:var(--muted)}
.welcome-btn{left:75px;top:989px;width:158px;height:48px;line-height:48px}
.hours{left:536px;top:645px;width:664px;height:465px;display:grid;grid-template-columns:repeat(3,1fr);grid-template-rows:repeat(2,1fr)}
.day{display:flex;flex-direction:column;align-items:center;justify-content:center;color:var(--white);font-size:15px;line-height:28px}
.day h3{font-family:"Josefin Sans",sans-serif;font-weight:400;font-size:22px;margin-bottom:14px}
.day.dark{background:var(--royal)}
.day.light{background:var(--sky)}

/* services */
.services{left:0;top:1110px;width:1200px;height:685px;background:var(--grey-bg)}
.section-title{width:1200px;text-align:center;font-family:"Josefin Sans",sans-serif;font-size:36px;font-weight:300;color:#6b6b6b;letter-spacing:1px}
.service{width:320px}
.service-head{display:flex;align-items:center;gap:14px;height:40px}
.service-head h4{font-family:"Josefin Sans",sans-serif;font-weight:400;font-size:20px;color:#555;letter-spacing:.5px}
.service-icon{width:44px;height:40px;display:flex;align-items:center;justify-content:center}
.pet-icon{width:34px;height:34px;border-radius:50%;background:var(--royal)}
.service p{margin:28px 0 0 70px;width:250px;font-size:13px;line-height:25px;color:var(--muted)}

/* team */
.team-arrows{left:1066px;top:1857px;display:flex;gap:6px}
.arrow{width:27px;height:27px;border-radius:50%;display:flex;align-items:center;justify-content:center}
.arrow.prev{background:var(--sky)}
.arrow.next{background:var(--royal)}
.card{top:2101px;width:242px;height:329px;background:var(--sky)}
.card h5{position:absolute;top:92px;width:100%;text-align:center;color:var(--white);font-family:"Josefin Sans",sans-serif;font-weight:600;font-size:16px}
.card p{position:absolute;top:128px;left:22px;width:198px;text-align:center;color:var(--white);font-size:12.5px;line-height:23px}
.portrait{top:1954px;width:176px;height:176px;border-radius:50%;border:4px solid var(--white);background:linear-gradient(160deg,#c9b7a4,#8d7a6a)}
.card-btn{top:2400px;width:158px;height:43px;line-height:43px}
.view-all{left:523px;top:2527px;width:156px;height:45px;line-height:45px}

/* map */
.map{left:0;top:2633px;width:1200px;height:351px;background:linear-gradient(135deg,#ecebe8,#e2e1de 60%,#f0efec)}

/* footer */
.site-footer{color:var(--white)}
.footer-band{left:0;top:2984px;width:1200px;height:333px;background:var(--footer)}
.foot-col{top:3068px;color:var(--white)}
.foot-col h6{font-family:"Oswald",sans-serif;font-weight:500;font-size:22px;letter-spacing:.5px;margin-bottom:28px;color:var(--white)}
.foot-col p,.foot-col li{font-size:13.5px;line-height:17.5px;list-style:none;color:var(--white)}
.contact-line{display:flex;align-items:center;gap:10px}
.hours-table{border-collapse:collapse}
.hours-table td{font-size:13.5px;line-height:17.5px;padding:0 24px 0 0;color:var(--white);white-space:nowrap}
.bottom-bar{left:72px;top:3345px;width:1056px;display:flex;justify-content:space-between;font-size:12px;color:var(--copyright)}
.bottom-bar span{margin-left:50px}
</style>
</head>
<body>

<header>
  <div class="abs brand"><span class="brand-dot"></span><span class="brand-name">Dr. Helmut Wenzlaff</span></div>
  <nav class="abs nav">
    <a class="active" href="#">Home</a>
    <a href="#">About us</a>
    <a href="#">Services</a>
    <a href="#">Practice</a>
    <a href="#">Team</a>
    <a href="#">Office Hours</a>
    <a href="#">Contact us</a>
  </nav>
</header>

<section>
  <div class="abs hero" role="img" aria-label="Smiling veterinarian in a white coat with a fluffy white dog on a bright clinic table"></div>
  <h1 class="abs hero-title">VETERINARY CLINIC</h1>
  <p class="abs hero-sub">Care for your Veterinar</p>
  <p class="abs hero-text">Lorem Ipsum is simply dummy text of the printing and typesetting industry. Lorem Ipsum has been the industry's standard dummy text ever since the 1500s.</p>
  <a class="abs btn hero-btn" href="#">Request An Appoinment</a>
</section>

<section>
  <h2 class="abs welcome-title">WELCOME</h2>
  <h3 class="abs welcome-kicker">OFFICE HOURS WITHOUT APPOINTMENT</h3>
  <p class="abs welcome-text">Welcome to the homepage of the veterinary practice of Dr. med. Helmut Wenzlaff. My team and I have put together information about the practice and information for patients.</p>
  <a class="abs btn welcome-btn" href="#">Learn More</a>
  <div class="abs hours">
    <div class="day dark"><h3>Monday</h3>9:30 - 11:00<br>16:00 - 19:00</div>
    <div class="day light"><h3>Tuesday</h3>9:30 - 11:00<br>16:00 - 19:00</div>
    <div class="day dark"><h3>Wednesday</h3>9:30 - 11:00<br>16:00 - 19:00</div>
    <div class="day light"><h3>Thursday</h3>16:00 - 19:00</div>
    <div class="day dark"><h3>Friday</h3>9:30 - 11:00<br>16:00 - 19:00</div>
    <div class="day light"><h3>Saturday</h3>9:30 - 11:00</div>
  </div>
</section>

<section>
  <div class="abs services"></div>
  <h2 class="abs section-title" style="top:1196px">OUR SERVICE</h2>

  <div class="abs service" style="left:80px;top:1338px">
    <div class="service-head"><div class="service-icon"><span class="pet-icon" role="img" aria-label="Dog icon"></span></div><h4>DOGS</h4></div>
    <p>you want to share your life with one or more dogs or are you already doing it?.</p>
  </div>
  <div class="abs service" style="left:453px;top:1338px">
    <div class="service-head"><div class="service-icon"><span class="pet-icon" role="img" aria-label="Cat icon"></span></div><h4>CATS</h4></div>
    <p>Together with you, we want to enable your cat to live a healthy, long life, and among other things offer you.</p>
  </div>
  <div class="abs service" style="left:826px;top:1338px">
    <div class="service-head"><div class="service-icon"><span class="pet-icon" role="img" aria-label="Small animal icon"></span></div><h4>SMALL ANIMALS</h4></div>
    <p>In the category "small mammals" fall many very different animal species in their needs.</p>
  </div>
  <div class="abs service" style="left:80px;top:1547px">
    <div class="service-head"><div class="service-icon"><svg width="40" height="40" viewBox="0 0 40 40"><circle cx="20" cy="20" r="13" fill="none" stroke="var(--royal)" stroke-width="4"/><circle cx="20" cy="20" r="5" fill="var(--royal)"/><path d="M20 2v10M20 28v10M2 20h10M28 20h10" stroke="var(--royal)" stroke-width="4"/></svg></div><h4>FOCUS</h4></div>
    <p>you want to share your life with one or more dogs or are you already doing it?.</p>
  </div>
  <div class="abs service" style="left:453px;top:1547px">
    <div class="service-head"><div class="service-icon"><svg width="38" height="38" viewBox="0 0 24 24"><path d="M12 1.5l3.2 6.8 7.3.9-5.4 5 1.4 7.3L12 17.9l-6.5 3.6 1.4-7.3-5.4-5 7.3-.9z" fill="var(--royal)"/></svg></div><h4>SPECIAL SERVICES</h4></div>
    <p>The practice offers the following special care and consulting services</p>
  </div>
  <div class="abs service" style="left:826px;top:1547px">
    <div class="service-head"><div class="service-icon"><svg width="36" height="36" viewBox="0 0 36 36"><path d="M12 0h12v12h12v12H24v12H12V24H0V12h12z" fill="var(--royal)"/></svg></div><h4>MEDICAL INSTITUTIONS</h4></div>
    <p>Among other things, the practice has the following medical facilities for examination and treatment.</p>
  </div>
</section>

<section>
  <h2 class="abs section-title" style="top:1852px">MEET OUR TEAM</h2>
  <div class="abs team-arrows">
    <span class="arrow prev"><svg width="12" height="12" viewBox="0 0 12 12"><path d="M8 1L3 6l5 5" fill="none" stroke="#fff" stroke-width="2"/></svg></span>
    <span class="arrow next"><svg width="12" height="12" viewBox="0 0 12 12"><path d="M4 1l5 5-5 5" fill="none" stroke="#fff" stroke-width="2"/></svg></span>
  </div>

  <div class="abs card" style="left:72px"><h5>DR. HELMUT WENZLAFF</h5><p>Lorem Ipsum is simply dummy text of the printing and typesetting industry. Lorem Ipsum has been the industry's standard dummy text ever since the 1500s.</p></div>
  <div class="abs card" style="left:340px"><h5>DR. BARBARA LINDQVIST</h5><p>Lorem Ipsum is simply dummy text of the printing and typesetting industry. Lorem Ipsum has been the industry's standard dummy text ever since the 1500s.</p></div>
  <div class="abs card" style="left:607px"><h5>DR. HELMUT WENZLAFF</h5><p>Lorem Ipsum is simply dummy text of the printing and typesetting industry. Lorem Ipsum has been the industry's standard dummy text ever since the 1500s.</p></div>
  <div class="abs card" style="left:876px"><h5>KASSANDRA VOLLMER</h5><p>Lorem Ipsum is simply dummy text of the printing and typesetting industry. Lorem Ipsum has been the industry's standard dummy text ever since the 1500s.</p></div>

  <div class="abs portrait" style="left:105px" role="img" aria-label="Portrait photo of team member"></div>
  <div class="abs portrait" style="left:373px" role="img" aria-label="Portrait photo of team member"></div>
  <div class="abs portrait" style="left:640px" role="img" aria-label="Portrait photo of team member"></div>
  <div class="abs portrait" style="left:909px" role="img" aria-label="Portrait photo of team member"></div>

  <a class="abs btn card-btn" style="left:114px" href="#">Read More</a>
  <a class="abs btn card-btn" style="left:382px" href="#">Read More</a>
  <a class="abs btn card-btn" style="left:649px" href="#">Read More</a>
  <a class="abs btn card-btn" style="left:918px" href="#">Read More</a>

  <a class="abs btn view-all" href="#">View All</a>
</section>

<div class="abs map" role="img" aria-label="Street map showing the practice location near the station"></div>

<footer class="site-footer">
  <div class="abs footer-band"></div>
  <div class="abs foot-col" style="left:72px;width:230px">
    <h6>ABOUT US</h6>
    <p>Welcome to the homepage of the veterinary practice of Dr. med. Helmut Wenzlaff.</p>
    <p style="margin-top:14px;display:flex;align-items:center;gap:8px">Read More... <svg width="16" height="16" viewBox="0 0 16 16"><circle cx="8" cy="8" r="6.5" fill="none" stroke="#fff" stroke-width="1.3"/><path d="M7 5l3 3-3 3" fill="none" stroke="#fff" stroke-width="1.3"/></svg></p>
  </div>
  <div class="abs foot-col" style="left:349px">
    <h6>QUICK LINK</h6>
    <ul><li>Home</li><li>About us</li><li>Services</li><li>Practice</li><li>Team</li><li>Office Hours</li><li>Contact us</li></ul>
  </div>
  <div class="abs foot-col" style="left:559px">
    <h6>USEFUL LINKS</h6>
    <p class="contact-line"><svg width="12" height="12" viewBox="0 0 24 24"><path d="M6.6 10.8a15 15 0 006.6 6.6l2.2-2.2c.3-.3.7-.4 1-.2 1.1.4 2.3.6 3.6.6.6 0 1 .4 1 1V20c0 .6-.4 1-1 1A17 17 0 013 4c0-.6.4-1 1-1h3.5c.6 0 1 .4 1 1 0 1.3.2 2.5.6 3.6.1.3 0 .7-.2 1z" fill="#fff"/></svg>030/555 01 23</p>
    <p class="contact-line"><svg width="12" height="12" viewBox="0 0 24 24"><rect x="3" y="3" width="18" height="18" rx="2" fill="#fff"/></svg>030/555 01 24</p>
    <p class="contact-line"><svg width="12" height="12" viewBox="0 0 24 24"><path d="M2 5h20v14H2z" fill="#fff"/><path d="M2 5l10 8 10-8" fill="none" stroke="#0a4ea2" stroke-width="2"/></svg>info@helmutwenzlaff.de</p>
    <p class="contact-line"><svg width="12" height="12" viewBox="0 0 24 24"><path d="M12 2a7 7 0 00-7 7c0 5 7 13 7 13s7-8 7-13a7 7 0 00-7-7zm0 9.5A2.5 2.5 0 1112 6.5a2.5 2.5 0 010 5z" fill="#fff"/></svg>12345 Berlin (Südviertel)</p>
  </div>
  <div class="abs foot-col" style="left:844px">
    <h6>OPENING HOURS</h6>
    <table class="hours-table">
      <tr><td>Monday</td><td>9:30 - 11:00</td><td>16:00 - 19:00</td></tr>
      <tr><td>Tuesday</td><td>9:30 - 11:00</td><td>16:00 - 19:00</td></tr>
      <tr><td>Wednesday</td><td>9:30 - 11:00</td><td>16:00 - 19:00</td></tr>
      <tr><td>Thursday</td><td>16:00 - 19:00</td><td></td></tr>
      <tr><td>Friday</td><td>9:30 - 11:00</td><td>16:00 - 19:00</td></tr>
      <tr><td>Saturday</td><td>9:30 - 11:00</td><td></td></tr>
    </table>
  </div>
  <div class="abs bottom-bar">
    <div>Copyright © 2019, Helmut Wenzlaff. All Right Reserved</div>
    <div><span>Privacy Policy</span><span>Terms &amp; Conditions</span></div>
  </div>
</footer>

</body>
</html>
```